Business card for Quorvane LLC | ||
Design a business card for a geospatial startup | ||
Use same font as used in my logo | ||
Cutting-Edge Corporate Modern Professional Simple |
Peter Hollis | ||
Chief Technical Officer | ||
48 Linden Row Suite 200 Bramwick, ST, 55821-3307 |
hello@quorvane-mail.net | ||
www.quorvane-site.net | ||
I''l provide the actual information once we get rolling :) I'd like to incorporate the corporate logo onto the card. Please keep the colors in the logo. You can use any font that looks good. |

```html
<!DOCTYPE html>
<html lang="en">
<head>
<meta charset="utf-8">
<title>Quorvane LLC — Business Card</title>
<link rel="stylesheet" href="https://fonts.googleapis.com/css2?family=Open+Sans:wght@400;600;700&family=Tinos&display=swap">
<style>
  :root {
    --backdrop: #d9dadc;
    --card-white: #ffffff;
    --brand-blue: #2d5c9f;
    --brand-blue-dark: #284f8c;
    --brand-green: #7dc242;
    --ink: #1f1f1f;
    --divider: #c9c9c9;
  }
  * { margin: 0; padding: 0; box-sizing: border-box; }
  html, body {
    width: 1200px; height: 780px; overflow: hidden;
    background: var(--backdrop);
  }
  .canvas { position: relative; width: 1200px; height: 780px; }
  .business-card {
    position: absolute; left: 100px; top: 90px;
    width: 1000px; height: 600px;
    background: var(--card-white);
    border-radius: 26px;
    overflow: hidden;
  }
  .card-bands { position: absolute; inset: 0; width: 1000px; height: 600px; }
  .band-blue { fill: var(--brand-blue); }
  .band-green { fill: var(--brand-green); }

  .holder {
    position: absolute; left: 62px; top: 110px;
    color: var(--card-white);
    font-family: "Open Sans", sans-serif;
  }
  .holder-name { font-size: 34px; font-weight: 700; line-height: 1.2; }
  .holder-title { font-size: 22px; font-weight: 400; line-height: 1.4; }

  .brand {
    position: absolute; left: 280px; top: 330px;
    display: flex; align-items: center; gap: 18px;
  }
  .brand-dot {
    width: 30px; height: 30px; border-radius: 50%;
    background: var(--brand-green);
  }
  .brand-name {
    font-family: "Open Sans", sans-serif;
    font-weight: 700; font-size: 84px; letter-spacing: -1px;
    color: var(--brand-blue-dark); line-height: 1;
  }

  .address {
    position: absolute; right: 530px; top: 448px;
    text-align: right;
    font-family: "Tinos", serif; font-size: 25px; line-height: 1.38;
    color: var(--ink);
  }
  .contact-divider {
    position: absolute; left: 498px; top: 440px;
    width: 2px; height: 120px; background: var(--divider);
  }
  .contacts {
    position: absolute; left: 518px; top: 432px;
    list-style: none;
    font-family: "Tinos", serif; font-size: 25px; color: var(--ink);
  }
  .contacts li { display: flex; align-items: center; gap: 12px; height: 42px; }
  .contact-icon { width: 22px; height: 22px; flex: none; }
  .contact-icon path, .contact-icon circle, .contact-icon ellipse, .contact-icon line {
    stroke: var(--brand-blue); fill: none; stroke-width: 2;
  }
  .contact-icon .solid { fill: var(--brand-blue); stroke: none; }
</style>
</head>
<body>
<main class="canvas">
  <article class="business-card">
    <svg class="card-bands" viewBox="0 0 1000 600" aria-hidden="true">
      <path class="band-blue" d="M0,0 H1000 V40 C700,60 350,200 0,390 Z"/>
      <path class="band-green" d="M1000,56 C700,76 350,216 20,430 C360,250 700,110 1000,96 Z"/>
    </svg>

    <header class="holder">
      <h1 class="holder-name">Peter Hollis</h1>
      <p class="holder-title">Chief Technical Officer</p>
    </header>

    <div class="brand">
      <span class="brand-name">Quorvane</span>
      <span class="brand-dot"></span>
    </div>

    <address class="address">
      48 Linden Row<br>
      Suite 200<br>
      Bramwick, ST, 55821-3307
    </address>

    <div class="contact-divider"></div>

    <ul class="contacts">
      <li>
        <svg class="contact-icon" viewBox="0 0 22 22" aria-hidden="true">
          <path class="solid" d="M5,2 L9,6 L7,9 C8,12 10,14 13,15 L16,13 L20,17 L17,20 C10,20 2,12 2,5 Z"/>
        </svg>
        <span>(800) 555-0142</span>
      </li>
      <li>
        <svg class="contact-icon" viewBox="0 0 22 22" aria-hidden="true">
          <circle cx="11" cy="11" r="4"/>
          <path d="M15,8 V13 C15,15 19,15 19,11 A8,8 0 1 0 15,18"/>
        </svg>
        <span>hello@quorvane-mail.net</span>
      </li>
      <li>
        <svg class="contact-icon" viewBox="0 0 22 22" aria-hidden="true">
          <circle cx="11" cy="11" r="9"/>
          <ellipse cx="11" cy="11" rx="4" ry="9"/>
          <line x1="2" y1="11" x2="20" y2="11"/>
        </svg>
        <span>www.quorvane-site.net</span>
      </li>
    </ul>
  </article>
</main>
</body>
</html>
```